Need Bold and Innovative Book Cover

Hi,

I am in need of a bold and innovative book cover to catch the attention of people.

Here is what the book is about:

Title: Quiet Harvest - Taming Clutter To Build Your Calmest Season Yet

Author: Captain Dale Farrow

This book is about how to eliminate overwhelm, stress, and information overload from your life. This book is a guide to teach people how I made my life better by getting rid of all kinds of stress, overwhelm, etc.

I have an information product that we created the book from. You can watch the video here to have an even better idea.

http://quietharvestbook.example/

In addition here is an instructional video about what I would like to see for the cover.

http://clipvault.example/t/QpRtZkLmWvA

I look forward to the designs.

Thanks!
Updates

Project Deadline Extended
Reason: Several designers needed a bit more time.

Project Deadline Extended
Reason: Need more time to work on this. Dale

Target Market(s)

Busy people who want to get more done.

Industry/Entity Type

Product

Requirements
Must have
• Model the info product so it all ties in but also use your own creativity.

```html
<!DOCTYPE html>
<html lang="en">
<head>
<meta charset="utf-8">
<title>Quiet Harvest — Book Cover</title>
<link rel="stylesheet" href="https://fonts.googleapis.com/css2?family=Barlow+Semi+Condensed:wght@600;700&family=Saira+Condensed:wght@800&display=swap">
<style>
  :root {
    --title-red-top: #e8313a;
    --title-red-bottom: #c4141f;
    --bg-top: #17161b;
    --bg-mid: #25243f;
    --bg-bottom: #3a3781;
    --scope-top: #9cccf2;
    --scope-mid: #7a93d2;
    --scope-bottom: #4c4894;
    --scope-ring: #2b2a33;
    --overlay-text: rgba(60, 62, 84, 0.6);
    --arrow-red: #e3141f;
    --white: #ffffff;
  }
  html, body {
    margin: 0;
    padding: 0;
    overflow: hidden;
  }
  body {
    width: 800px;
    height: 1200px;
  }
  .cover {
    position: relative;
    width: 800px;
    height: 1200px;
    overflow: hidden;
    background: linear-gradient(180deg, var(--bg-top) 0%, var(--bg-mid) 45%, var(--bg-bottom) 100%);
  }
  .title {
    position: absolute;
    top: 14px;
    left: 0;
    width: 100%;
    margin: 0;
    text-align: center;
    font-family: "Saira Condensed", "Barlow Semi Condensed", sans-serif;
    font-weight: 800;
    font-size: 136px;
    line-height: 112px;
    letter-spacing: 3px;
    text-transform: uppercase;
    background: linear-gradient(180deg, var(--title-red-top), var(--title-red-bottom));
    -webkit-background-clip: text;
    background-clip: text;
    color: transparent;
  }
  .title span { display: block; }
  .subtitle {
    position: absolute;
    top: 248px;
    left: 0;
    width: 100%;
    margin: 0;
    text-align: center;
    font-family: "Barlow Semi Condensed", sans-serif;
    font-weight: 700;
    font-size: 31px;
    line-height: 36px;
    letter-spacing: 0.5px;
    color: var(--white);
    text-transform: uppercase;
  }
  .scope {
    position: absolute;
    left: 72px;
    top: 298px;
    width: 656px;
    height: 656px;
    box-sizing: border-box;
    border-radius: 50%;
    border: 8px solid var(--scope-ring);
    background: linear-gradient(180deg, var(--scope-top) 0%, var(--scope-mid) 50%, var(--scope-bottom) 100%);
  }
  .scope-label {
    position: absolute;
    left: 0;
    top: 240px;
    width: 100%;
    margin: 0;
    text-align: center;
    font-family: "Barlow Semi Condensed", sans-serif;
    font-weight: 700;
    font-size: 56px;
    line-height: 70px;
    letter-spacing: 2px;
    color: var(--overlay-text);
    text-transform: uppercase;
  }
  .scope-label span { display: block; }
  .growth-arrow {
    position: absolute;
    left: 0;
    top: 0;
    width: 800px;
    height: 1200px;
  }
  .author {
    position: absolute;
    right: 22px;
    top: 968px;
    margin: 0;
    text-align: right;
    font-family: "Barlow Semi Condensed", sans-serif;
    font-weight: 700;
    font-size: 60px;
    line-height: 86px;
    color: var(--white);
  }
  .author span { display: block; }
</style>
</head>
<body>
<main class="cover">
  <h1 class="title"><span>Quiet</span><span>Harvest</span></h1>
  <p class="subtitle">Taming Clutter to Build Your Calmest Season Yet</p>

  <div class="scope" role="img" aria-label="Rifle scope view with crosshair over a fence at dusk">
    <p class="scope-label"><span>Information</span><span>Overload</span></p>
  </div>

  <svg class="growth-arrow" viewBox="0 0 800 1200" xmlns="http://www.w3.org/2000/svg" aria-hidden="true">
    <polyline points="-12,1112 200,935 245,982 330,898 445,958 590,732" fill="none" stroke="var(--arrow-red)" stroke-width="20" stroke-linejoin="miter"/>
    <polygon points="637,652 627,758 547,707" fill="var(--arrow-red)"/>
  </svg>

  <p class="author"><span>Captain</span><span>Dale Farrow</span></p>
</main>
</body>
</html>
```